Tarsel Energy Letter Head- with all subsidiaries

We need a letterhead that will showcase all Tarsel Energy subsidiaries, while still have Tarsel Energy logo ontop.

```html
<!DOCTYPE html>
<html lang="en">
<head>
<meta charset="utf-8">
<title>Tarsel Energy Letterhead</title>
<link rel="stylesheet" href="https://fonts.googleapis.com/css2?family=Lato:wght@400;700;900&family=Yellowtail&display=swap">
<style>
  :root {
    --backdrop-light: #f1f2f3;
    --backdrop-dark: #cfd0d3;
    --paper: #ffffff;
    --paper-edge: #b9babd;
    --gold: #c9ad6a;
    --charcoal: #3f3f41;
    --ink: #3a3a3a;
    --white: #ffffff;
    --sky: #2fa4e0;
    --steel: #9a9ca0;
  }
  * { box-sizing: border-box; margin: 0; padding: 0; }
  html, body { width: 932px; height: 1200px; overflow: hidden; }
  body {
    position: relative;
    background: radial-gradient(ellipse at 50% 45%, var(--backdrop-light) 0%, var(--backdrop-dark) 100%);
    font-family: "Lato", Arial, sans-serif;
    color: var(--ink);
  }
  .letterhead {
    position: absolute;
    left: 42px; top: 51px;
    width: 848px; height: 1097px;
    background: var(--paper);
    border: 1px solid var(--paper-edge);
    overflow: hidden;
  }
  .brand {
    position: absolute;
    left: 290px; top: 104px;
    display: flex; align-items: center; gap: 12px;
  }
  .brand-mark { width: 34px; height: 34px; background: var(--gold); }
  .brand-name {
    font-weight: 900; font-size: 38px; letter-spacing: 2px;
    color: var(--charcoal); text-transform: uppercase;
  }
  .letter {
    position: absolute;
    left: 72px; top: 262px;
    width: 704px;
  }
  .salutation { font-weight: 700; font-size: 15px; color: var(--gold); margin-bottom: 20px; }
  .body-copy p {
    font-size: 15.6px; line-height: 25.2px;
    text-align: justify; margin-bottom: 18px;
  }
  .closing { font-size: 19px; margin-top: 26px; color: #222; }
  .signature { font-family: "Yellowtail", cursive; font-size: 32px; color: var(--gold); margin-top: 4px; }

  .footer-waves { position: absolute; left: 0; bottom: 0; width: 848px; height: 123px; }

  .subsidiary {
    position: absolute;
    display: flex; align-items: center; gap: 6px;
  }
  .subsidiary-mark { width: 12px; height: 12px; background: var(--gold); flex: none; }
  .subsidiary-name {
    font-weight: 900; font-size: 13px; line-height: 14px;
    color: var(--charcoal); text-transform: uppercase;
  }
  .subsidiary-electric .subsidiary-mark { background: var(--steel); border-radius: 50%; }
  .subsidiary-bright .subsidiary-mark { background: var(--sky); }

  .contact {
    position: absolute; right: 14px; top: 1012px;
    list-style: none; text-align: right;
  }
  .contact li {
    display: flex; justify-content: flex-end; align-items: center; gap: 6px;
    font-size: 13px; line-height: 20.5px; color: var(--white);
  }
  .contact svg { width: 12px; height: 12px; flex: none; }
</style>
</head>
<body>
  <main class="letterhead">
    <header class="brand">
      <span class="brand-mark"></span>
      <span class="brand-name">Tarsel Energy</span>
    </header>

    <section class="letter">
      <p class="salutation">Dear Mr. Lorem,</p>
      <div class="body-copy">
        <p>Lorem ipsum dolor sit amet, consectetuer adipiscing elit, sed diam nonummy nibh euismod tincidunt ut laoreet dolore magna aliquam erat volutpat. Ut wisi enim ad minim veniam, quis nostrud exerci tation ullamcorper suscipit lobortis nisl ut aliquip ex ea commodo consequat. Duis autem vel eum iriure dolor in hendiusto odio dignissim qui blandit praesent luptatum zzril delenit augue duis dolore te feugait nulla facilisi.</p>
        <p>Lorem ipsum dolor sit amet, consectetuer adipiscing elit, sed diam nonummy nibh euismod tincidunt ut laoreet dolore magna aliquam erat volutpat. Ut wisi enim ad minim veniam, quis nostrud exerci tation ullamcorper suscipit lobortis nisl ut aliquip ex ea commodo consequat. Duis autem vel eum iriure dolor in hendiusto odio dignissim qui blandit praesent luptatum zzril delenit augue duis dolore te feugait nulla facilisi.</p>
        <p>Lorem ipsum dolor sit amet, consectetuer adipiscing elit, sed diam nonummy nibh euismod tincidunt ut laoreet dolore magna aliquam erat volutpat. Ut wisi enim ad minim veniam, quis nostrud exerci tation ullamcorper suscipit lobortis nisl ut aliquip ex ea commodo consequat. Duis autem vel eum iriure dolor in hendiusto odio dignissim qui blandit praesent luptatum zzril delenit augue duis dolore te feugait nulla facilisi.</p>
      </div>
      <p class="closing">Sincerely Your,</p>
      <p class="signature">Your Name</p>
    </section>

    <svg class="footer-waves" viewBox="0 0 848 123" aria-hidden="true">
      <path d="M0,76 C250,95 550,40 848,4 L848,16 C560,52 260,108 0,90 Z" fill="var(--gold)"/>
      <path d="M0,98 C300,118 560,52 848,24 L848,123 L0,123 Z" fill="var(--charcoal)"/>
      <path d="M40,116 C320,122 560,72 848,38" fill="none" stroke="var(--white)" stroke-width="2"/>
    </svg>

    <div class="subsidiary subsidiary-electric" style="left:72px; top:1014px;">
      <span class="subsidiary-mark"></span><span class="subsidiary-name">Nordal<br>Electric</span>
    </div>
    <div class="subsidiary" style="left:182px; top:1004px;">
      <span class="subsidiary-mark"></span><span class="subsidiary-name">Tarsel<br>Aviation</span>
    </div>
    <div class="subsidiary" style="left:308px; top:980px;">
      <span class="subsidiary-mark"></span><span class="subsidiary-name">Tarsel<br>Acquisitions</span>
    </div>
    <div class="subsidiary" style="left:436px; top:952px;">
      <span class="subsidiary-mark"></span><span class="subsidiary-name">Tarsel<br>Logistics</span>
    </div>
    <div class="subsidiary" style="left:562px; top:930px;">
      <span class="subsidiary-mark"></span><span class="subsidiary-name">Tarsel<br>Caribbean</span>
    </div>
    <div class="subsidiary subsidiary-bright" style="left:690px; top:922px;">
      <span class="subsidiary-mark"></span><span class="subsidiary-name">Brightline<br>Electrical</span>
    </div>

    <ul class="contact">
      <li>
        <svg viewBox="0 0 12 12"><rect x="3" y="1" width="6" height="10" rx="1.2" fill="none" stroke="var(--gold)" stroke-width="1.2"/><circle cx="6" cy="9" r=".7" fill="var(--gold)"/></svg>
        012-345-6789
      </li>
      <li>
        <svg viewBox="0 0 12 12"><rect x="1" y="3" width="10" height="7" fill="none" stroke="var(--gold)" stroke-width="1.2"/><path d="M1 3 L6 7 L11 3" fill="none" stroke="var(--gold)" stroke-width="1.2"/></svg>
        assist@tarselenergy.com
      </li>
      <li>
        <svg viewBox="0 0 12 12"><circle cx="6" cy="6" r="5" fill="none" stroke="var(--gold)" stroke-width="1.1"/><ellipse cx="6" cy="6" rx="2.2" ry="5" fill="none" stroke="var(--gold)" stroke-width="1"/><path d="M1 6 H11" stroke="var(--gold)" stroke-width="1"/></svg>
        www.tarselenergy.com
      </li>
      <li>
        <svg viewBox="0 0 12 12"><path d="M6 11 C3 7.5 2 6 2 4.5 A4 4 0 0 1 10 4.5 C10 6 9 7.5 6 11 Z" fill="none" stroke="var(--gold)" stroke-width="1.2"/><circle cx="6" cy="4.6" r="1.3" fill="var(--gold)"/></svg>
        Street Name, City Name, Zipcode-01234
      </li>
    </ul>
  </main>
</body>
</html>
```